Dental Medical History Form - Content provided

Design a medical history form for a dental practice. Content is provided so all that is needed is the formatting to make it look great and easy to read.

"Patient Information" to include all information contained in top portion of the "Patient Medical History Form" docx file.

"Medical History" should follow the formatting and content of the "Exact Medical History" file as this is what the entry fields look like in our practice software and so we would like it to match.

1st page - Patient info, allergies, medications, antibiotics, joint replacement, pregnancy.

2nd page - Do you have, or have you had, any of the following? . . . . . . .
Updates

Project Deadline Extended Reason: Picked too short of a deadline to start (2 days) Added Monday, February 13, 2017

Target Market(s)

All ages but must be clear enough for elderly to read. Use as much space as possible to keep font size bigger yet keep to two pages

Industry/Entity Type

Dental

Font styles to use
Sans Serif

Requirements
Must have
• All content provided
• Our logo at the top (file provided)
• Century Gothic Font
• Limit to two pages

```html
<!DOCTYPE html>
<html lang="en">
<head>
<meta charset="utf-8">
<title>Harbourline Dental – Confidential Medical History</title>
<link rel="stylesheet" href="https://fonts.googleapis.com/css2?family=Questrial&family=PT+Sans+Narrow:wght@400;700&display=swap">
<style>
  :root{
    --ink:#2c3e4f;
    --text:#2b2f33;
    --line:#6a7179;
    --paper:#ffffff;
    --backdrop:#c9d9e6;
    --band-text:#ffffff;
  }
  *{box-sizing:border-box;margin:0;padding:0}
  html,body{width:1200px;height:784px;overflow:hidden}
  body{background:var(--backdrop);font-family:"PT Sans Narrow",Arial Narrow,sans-serif;color:var(--text)}
  .form-page{position:absolute;left:340px;top:24px;width:520px;height:736px;background:var(--paper);
    box-shadow:0 2px 10px rgba(40,60,80,.18);padding:22px 26px 0;font-size:9px}
  .masthead{display:flex;justify-content:space-between;align-items:flex-start}
  .practice-name{font-family:"Questrial",sans-serif;font-size:30px;color:var(--ink);line-height:1;letter-spacing:-.5px}
  .practice-contact{text-align:right;font-weight:700;font-size:8px;line-height:1.3;margin-top:26px}
  .form-title{font-family:"Questrial",sans-serif;font-weight:400;font-size:15px;letter-spacing:2.5px;color:var(--ink);
    margin:8px 0 8px;-webkit-text-stroke:.4px var(--ink)}
  .section-band{background:var(--ink);color:var(--band-text);font-weight:700;font-size:9px;text-align:center;
    height:14px;line-height:14px;margin:8px -26px 8px -26px;padding:0 26px}
  .field-row{display:flex;align-items:center;gap:5px;height:23px}
  .field-label{white-space:nowrap}
  .entry-box{flex:1;height:15px;border:1px solid var(--line)}
  .title-chip{border:1px solid var(--line);padding:0 3px;font-size:8px;font-style:italic;height:12px;line-height:10px}
  .digit-box{width:11px;height:13px;border:1px solid var(--line);display:inline-block}
  .digit-gap{margin-right:4px}
  .tick-box{width:9px;height:9px;border:1px solid var(--line);display:inline-block;margin:0 8px 0 3px;vertical-align:middle}
  .choice-row{display:flex;justify-content:space-between;align-items:center;height:20px}
  .choice{white-space:nowrap}
  .rule-lines{display:grid;grid-template-columns:1fr 1fr;column-gap:20px;row-gap:15px;margin:10px 0 14px}
  .rule-lines span{border-bottom:1px solid var(--line);height:1px}
  .question-row{display:flex;align-items:center;height:20px}
  .question-row .field-label{width:150px}
  .page-foot{position:absolute;left:0;right:0;bottom:0;height:10px;background:var(--ink)}
  .turn-tab{position:absolute;right:26px;bottom:0;width:118px;height:24px;background:var(--ink);color:var(--band-text);
    border-radius:6px 6px 0 0;font-weight:700;font-size:9px;text-align:center;line-height:22px}
</style>
</head>
<body>
<main class="form-page">
  <header class="masthead">
    <div class="practice-name">Harbourline Dental</div>
    <address class="practice-contact">Suite 4/18 Seaview Rd,<br>Tamsworth NSW 2000<br>(02) 5550 1234</address>
  </header>
  <h1 class="form-title">CONFIDENTIAL MEDICAL HISTORY</h1>

  <div class="section-band">General Information</div>
  <div class="field-row"><span class="field-label">Name:</span><span class="title-chip">Mr</span><span class="title-chip">Miss</span><span class="title-chip">Mrs</span><span class="field-label">Last</span><span class="entry-box"></span><span class="field-label">First</span><span class="entry-box"></span><span class="field-label">DOB:</span><span><i class="digit-box"></i><i class="digit-box digit-gap"></i><i class="digit-box"></i><i class="digit-box digit-gap"></i><i class="digit-box"></i><i class="digit-box"></i><i class="digit-box"></i><i class="digit-box"></i></span></div>
  <div class="field-row"><span class="field-label">Address:</span><span class="entry-box"></span></div>
  <div class="field-row"><span class="field-label">Email Address:</span><span class="entry-box"></span></div>
  <div class="field-row"><span class="field-label">Phone Number(s): Mobile</span><span class="entry-box"></span><span class="field-label">Home</span><span class="entry-box"></span><span class="field-label">Work</span><span class="entry-box"></span></div>
  <div class="field-row"><span class="field-label">Emergency Contact Person: Name:</span><span class="entry-box"></span><span class="field-label">Relationship:</span><span class="entry-box"></span><span class="field-label">Phone number:</span><span class="entry-box"></span></div>
  <div class="field-row"><span class="field-label">General Practitioner Name:</span><span class="entry-box"></span><span class="field-label">Phone:</span><span class="entry-box"></span></div>
  <div class="field-row"><span class="field-label">Do you have dental health fund cover?</span><span class="choice">Yes<i class="tick-box"></i>or<i class="tick-box"></i>No</span><span class="field-label">If so, what is the name of the fund?</span><span class="entry-box"></span></div>
  <div class="field-row"><span class="field-label">Fund Number:</span><span class="entry-box"></span><span class="field-label">Priority Number on card: 0<i class="tick-box"></i>1<i class="tick-box"></i>2<i class="tick-box"></i>3<i class="tick-box"></i>4<i class="tick-box"></i>5<i class="tick-box"></i>6</span></div>
  <div class="field-row"><span class="field-label">Occupation:</span><span class="entry-box"></span><span class="field-label">Referred by:</span><span class="entry-box"></span></div>

  <div class="section-band">Please indicate if you are allergic to any of the following?</div>
  <div class="choice-row"><span class="choice">Aspirin<i class="tick-box"></i></span><span class="choice">Codeine<i class="tick-box"></i></span><span class="choice">Penicillin<i class="tick-box"></i></span><span class="choice">Sulfites<i class="tick-box"></i></span><span class="choice">Latex<i class="tick-box"></i></span><span class="choice">Local Anaesthetic<i class="tick-box"></i></span><span class="choice">Lactose<i class="tick-box"></i></span><span class="choice">Nickel<i class="tick-box"></i></span></div>
  <div class="field-row"><span class="field-label">Other:</span><span class="entry-box"></span></div>

  <div class="section-band">Are you currently taking, or have ever taken, any of the following medications?</div>
  <div class="choice-row"><span class="choice">Asthma inhaler<i class="tick-box"></i></span><span class="choice">Anti-epileptics<i class="tick-box"></i></span><span class="choice">Anti-depressants<i class="tick-box"></i></span><span class="choice">Blood Pressure<i class="tick-box"></i></span><span class="choice">Blood Thinners<i class="tick-box"></i></span><span class="choice">Bisphosphonates<i class="tick-box"></i></span></div>
  <div class="choice-row"><span class="choice">Chemotherapy<i class="tick-box"></i></span><span class="choice">Insulin<i class="tick-box"></i></span><span class="choice">Immunosuppressants<i class="tick-box"></i></span><span class="choice">Steroids<i class="tick-box"></i></span><span class="choice">Oral Contraceptive<i class="tick-box"></i></span><span class="choice">Other<i class="tick-box"></i></span></div>

  <div class="section-band">Please specify medication name, dose, and frequency where possible:</div>
  <div class="rule-lines"><span></span><span></span><span></span><span></span><span></span><span></span></div>

  <div class="question-row"><span class="field-label">Do you require antibiotic cover?</span><span class="choice">Yes<i class="tick-box"></i>No<i class="tick-box"></i></span></div>
  <div class="question-row"><span class="field-label">Have you had a joint replacement?</span><span class="choice">Yes<i class="tick-box"></i>No<i class="tick-box"></i></span></div>
  <div class="question-row"><span class="field-label">Women: Are you pregnant?</span><span class="choice">Yes<i class="tick-box"></i>No<i class="tick-box"></i>Possible<i class="tick-box"></i>How Many Weeks?<i class="digit-box" style="margin-left:4px"></i><i class="digit-box"></i></span></div>

  <div class="page-foot"></div>
  <div class="turn-tab">Please Turn Over</div>
</main>
</body>
</html>
```